Rural contractor needs professional informative business card

We need a business card design that looks professional but also includes information about the services that the business offers.
The business is an earthmoving and transport business. All of the services offered are listed on the old card attached.
The business is aimed at farmers so the design we are after is a classic look. The card needs to include all of the information that is listed on the old card design uploaded as an attachment. We recognize that this is a lot of information to fit on a business card but it also operates as a key marketing tool so is very important to the business.
Feel free to send me your questions.
Thanks
Reason: We are having trouble deciding between all these great designs - thank you for your efforts
We would love to see some designs using red with a little white and black. Also feel free to re-design our logo if you feel it needs to be to fit your designs. Thank you

```html
<!DOCTYPE html>
<html lang="en">
<head>
<meta charset="utf-8">
<title>Brennan Contracting – Business Card</title>
<link rel="stylesheet" href="https://fonts.googleapis.com/css2?family=Ubuntu:wght@500;700&display=swap">
<style>
  :root {
    --bg: #e8e8e8;
    --card: #f2f2f2;
    --ink: #151515;
    --band: #1a1a1a;
    --red: #d7141f;
    --white: #ffffff;
    --rule: #8a8a8a;
  }
  * { margin: 0; padding: 0; box-sizing: border-box; }
  html, body {
    width: 1200px; height: 900px; overflow: hidden;
    background: var(--bg);
    font-family: "Ubuntu", sans-serif;
    color: var(--ink);
  }
  .canvas {
    position: relative; width: 1200px; height: 900px;
  }
  .card {
    position: absolute; left: 280px;
    width: 640px; height: 391px;
    background: var(--card);
    box-shadow: 0 6px 18px rgba(0,0,0,.18);
    overflow: hidden;
  }
  .card--services { top: 39px; }
  .card--contact { top: 470px; }
  .card-shapes { position: absolute; inset: 0; }
  .brand {
    position: absolute;
    display: flex; align-items: center; gap: 8px;
    color: var(--red); font-weight: 700; font-size: 24px;
    letter-spacing: .2px; white-space: nowrap;
  }
  .brand-mark { width: 12px; height: 12px; background: var(--red); }
  .brand-rule { position: absolute; height: 2px; background: var(--rule); }

  /* services side */
  .card--services .brand { right: 26px; top: 30px; }
  .card--services .brand-rule { right: 26px; top: 70px; width: 240px; }
  .band-title {
    position: absolute; right: 24px;
    color: var(--white); font-weight: 700; font-size: 30px; line-height: 1;
  }
  .band-title--earth { top: 101px; }
  .band-title--transport { top: 262px; }
  .service-list {
    position: absolute; right: 26px; top: 146px;
    list-style: none; text-align: right;
    font-weight: 700; font-size: 19px; line-height: 25px;
  }
  .cargo-list {
    position: absolute; right: 60px; top: 306px;
    display: grid; grid-template-columns: auto auto; column-gap: 34px; row-gap: 4px;
    list-style: none; font-weight: 700; font-size: 19px;
  }

  /* contact side */
  .card--contact .brand { left: 30px; top: 28px; }
  .card--contact .brand-rule--top { left: 30px; top: 66px; width: 290px; }
  .person {
    position: absolute; left: 30px; top: 82px;
    font-weight: 500; font-size: 25px;
  }
  .card--contact .brand-rule--name { left: 30px; top: 122px; width: 330px; }
  .contact-details {
    position: absolute; left: 30px; top: 134px;
    font-style: normal; font-weight: 700; font-size: 20px; line-height: 28px;
  }
  .contact-details .phone { margin-bottom: 8px; font-size: 21px; }
  .tagline {
    position: absolute; left: 26px; top: 307px;
    color: var(--white); font-weight: 700; font-size: 31px; white-space: nowrap;
  }
</style>
</head>
<body>
<main class="canvas">

  <!-- Services side -->
  <section class="card card--services" aria-label="Services side of business card">
    <svg class="card-shapes" viewBox="0 0 640 391" width="640" height="391">
      <defs>
        <linearGradient id="truckTones" x1="0" y1="0" x2="0" y2="1">
          <stop offset="0" stop-color="#2f5fa8"/>
          <stop offset=".45" stop-color="#d9d6cf"/>
          <stop offset=".8" stop-color="#b9a888"/>
          <stop offset="1" stop-color="#8c7a5c"/>
        </linearGradient>
      </defs>
      <g role="img" aria-label="Photo of a white prime mover truck under a blue sky">
        <polygon points="0,0 400,0 140,391 0,391" fill="url(#truckTones)"/>
      </g>
      <polygon points="400,0 424,0 164,391 140,391" fill="var(--band)"/>
      <line x1="400" y1="0" x2="140" y2="391" stroke="var(--red)" stroke-width="4"/>
      <polygon points="334,100 640,100 640,140 307,140" fill="var(--band)"/>
      <polygon points="229,258 640,258 640,298 202,298" fill="var(--band)"/>
    </svg>
    <div class="brand"><span class="brand-mark"></span>Brennan Contracting</div>
    <div class="brand-rule"></div>
    <h2 class="band-title band-title--earth">Earthmoving</h2>
    <ul class="service-list">
      <li>Road Building &amp; Maintenance</li>
      <li>Poly Pipe Laying</li>
      <li>Clearing fence lines</li>
      <li>Sand &amp; Gravel Supplies</li>
    </ul>
    <h2 class="band-title band-title--transport">Transport</h2>
    <ul class="cargo-list">
      <li>Grain</li><li>Cotton</li>
      <li>Wool</li><li>Sand &amp; Gravel</li>
    </ul>
  </section>

  <!-- Contact side -->
  <section class="card card--contact" aria-label="Contact side of business card">
    <svg class="card-shapes" viewBox="0 0 640 391" width="640" height="391">
      <defs>
        <linearGradient id="graderTones" x1="0" y1="0" x2="0" y2="1">
          <stop offset="0" stop-color="#3d6fb5"/>
          <stop offset=".35" stop-color="#9bb6d6"/>
          <stop offset=".55" stop-color="#d9a72a"/>
          <stop offset="1" stop-color="#b8934e"/>
        </linearGradient>
      </defs>
      <g role="img" aria-label="Photo of a yellow motor grader on a dry paddock">
        <polygon points="368,0 640,0 640,300 460,300" fill="url(#graderTones)"/>
      </g>
      <polygon points="344,0 368,0 460,300 436,300" fill="var(--band)"/>
      <line x1="368" y1="0" x2="460" y2="300" stroke="var(--red)" stroke-width="4"/>
      <rect x="0" y="300" width="640" height="52" fill="var(--band)"/>
      <rect x="470" y="352" width="170" height="7" fill="var(--red)"/>
    </svg>
    <div class="brand"><span class="brand-mark"></span>Brennan Contracting</div>
    <div class="brand-rule brand-rule--top"></div>
    <h1 class="person">Callum Brennan</h1>
    <div class="brand-rule brand-rule--name"></div>
    <address class="contact-details">
      <div class="phone">0400 555 217</div>
      <div>47 Wattle Street</div>
      <div>Dunmore 2899</div>
      <div>callumbrennan@mailpost.com</div>
    </address>
    <p class="tagline">Earthmoving &amp; Transport Solutions</p>
  </section>

</main>
</body>
</html>
```